Bright And Steady Web Design & Marketing

Will award a 2nd place prize of $100.00 if someone can come up with a logo to match this design!
Updates

Okay, I'm really looking to see some better designs here. What do you think will bring the best designs out? Please remember with all future submissions I'm looking for a cartoon style / illustrator style website. I'm not sure what the technical term is for it, so I uploaded some images in the brief.

Target Market(s)

Small Business Owners

Industry/Entity Type

Marketing

Logo Text

BrightAndSteady.example

Number of Pages Required

1 page

Colors

Designer to choose colors to be used in the design.

Requirements
Must have
• Logo should say BrightAndSteady.example I would like more than just a text logo. I want some sort of cool custom graphic / icon with it that will look nice on shirts/hats/etc

```html
<!DOCTYPE html>
<html lang="en">
<head>
<meta charset="utf-8">
<title>Bright And Steady Web Design &amp; Marketing</title>
<link href="https://fonts.googleapis.com/css2?family=Raleway:wght@400;500;600;700;800&display=swap" rel="stylesheet">
<style>
:root{
  --red:#e0231b;
  --red-dark:#c81e17;
  --orange:#f9a61a;
  --yellow:#fbb911;
  --ink:#1f1f24;
  --navy:#2b3a67;
  --muted:#8a8a8a;
  --line:#e6e6e6;
  --paper:#ffffff;
  --mist:#f6f6f6;
}
*{box-sizing:border-box;margin:0;padding:0}
html,body{width:1200px;height:4045px;overflow:hidden}
body{font-family:'Raleway',sans-serif;color:var(--ink);background:var(--paper);position:relative}
a{color:inherit;text-decoration:none}

/* header */
.site-header{position:absolute;top:0;left:0;width:1200px;height:100px;background:var(--paper)}
.brand{position:absolute;left:81px;top:26px;display:flex;align-items:center;gap:12px}
.brand-dot{width:44px;height:44px;border-radius:50%;background:var(--orange);display:block}
.brand-name{font-weight:800;font-size:23px;color:var(--ink)}
.main-nav{position:absolute;right:80px;top:38px;display:flex;gap:20px;font-size:15px;font-weight:500}
.main-nav a.active{color:var(--orange)}

/* hero */
.hero{position:absolute;top:100px;left:0;width:1200px;height:590px}
.hero-photo{position:absolute;inset:0;background:linear-gradient(100deg,#5b5550 0%,#8b817a 30%,#c9beb4 55%,#e6dcd1 75%,#b5aaa1 100%)}
.hero-shade{position:absolute;inset:0;background:linear-gradient(90deg,rgba(20,16,14,.55) 0%,rgba(20,16,14,.25) 45%,rgba(20,16,14,0) 65%)}
.hero-copy{position:absolute;left:81px;top:175px;width:520px;color:#fff}
.hero-copy h1{font-size:33px;font-weight:800;line-height:1.28}
.hero-copy p{font-size:16px;line-height:1.5;margin-top:14px;width:520px}
.hero-actions{display:flex;gap:14px;margin-top:24px}
.btn{display:inline-flex;align-items:center;justify-content:center;height:42px;color:#fff;font-size:15px;font-weight:600}
.btn-orange{background:var(--orange)}
.btn-red{background:var(--red)}
.hero-actions .btn{width:202px}

/* section heads */
.section-title{position:absolute;left:0;width:1200px;text-align:center;font-size:30px;font-weight:800;color:var(--ink)}
.divider{position:absolute;left:550px;width:100px;height:24px}

/* services */
.services{position:absolute;top:690px;left:0;width:1200px;height:793px}
.service-grid{position:absolute;left:81px;top:172px;width:1040px;display:grid;grid-template-columns:repeat(4,1fr)}
.service{height:283px;padding-top:8px;text-align:center;border-left:1px solid var(--line)}
.service:nth-child(4n+1){border-left:none}
.service:nth-child(-n+4){border-bottom:1px solid var(--line)}
.service:nth-child(n+5){padding-top:18px}
.service svg{display:block;margin:0 auto}
.service h3{font-size:15px;font-weight:600;line-height:1.45;margin:14px auto 10px;width:210px}
.service p{font-size:11.5px;line-height:1.5;color:var(--muted);width:210px;margin:0 auto}
.services .btn{position:absolute;left:510px;top:758px;width:180px;height:43px}

/* about */
.about{position:absolute;top:1483px;left:0;width:1200px;height:702px}
.about svg.band{position:absolute;inset:0}
.about h2{position:absolute;top:192px;left:0;width:1200px;text-align:center;color:#fff;font-size:29px;font-weight:800}
.about-text{position:absolute;top:292px;left:81px;width:1040px;text-align:center;color:#fff;font-size:14px;line-height:2.1}
.about-text p+p{margin-top:20px}
.about .btn{position:absolute;left:510px;top:462px;width:180px;height:40px}

/* features */
.features{position:absolute;top:2185px;left:0;width:1200px;height:605px}
.feature-row{position:absolute;left:81px;top:108px;width:1040px;display:grid;grid-template-columns:repeat(4,1fr)}
.feature{text-align:center}
.feature svg{display:block;margin:0 auto}
.feature h3{font-size:15px;font-weight:600;line-height:1.45;margin:6px auto 8px;width:220px}
.feature p{font-size:12px;line-height:1.6;color:var(--muted);width:220px;margin:0 auto}
.feature .contact-line{display:flex;justify-content:center;align-items:center;gap:8px;font-size:13px;color:#555;line-height:2}
.feature .contact-line svg{margin:0}
.feature-solo{position:absolute;left:470px;top:318px;width:260px}
.feature-solo p{width:250px}

/* team */
.team{position:absolute;top:2790px;left:0;width:1200px;height:487px;background:var(--mist)}
.team-grid{position:absolute;left:81px;top:195px;display:flex;gap:24px}
.member{width:189px;height:225px;background:#fff;box-shadow:0 3px 8px rgba(0,0,0,.18)}
.member-photo{height:162px;background:linear-gradient(160deg,#d9d2cb,#9f958d)}
.member h4{font-size:13px;font-weight:600;margin:12px 12px 2px;text-transform:uppercase}
.member span{display:block;font-size:11.5px;color:var(--muted);margin:0 12px;text-transform:uppercase}

/* clients */
.clients{position:absolute;top:3277px;left:0;width:1200px;height:383px}
.client-row{position:absolute;top:188px;left:0;width:1200px;display:flex}
.client{width:200px;height:122px;display:flex;align-items:center;justify-content:center;gap:8px;border-right:1px solid var(--line);box-shadow:0 3px 5px rgba(0,0,0,.08);font-size:17px;font-weight:700;color:var(--navy)}
.client i{width:12px;height:12px;border-radius:50%;background:var(--navy);display:block}

/* footer */
.site-footer{position:absolute;top:3660px;left:0;width:1200px;height:305px;background:var(--red)}
.foot-col{position:absolute;top:60px;color:#fff;font-size:13px}
.foot-col h4{color:var(--yellow);font-size:17px;font-weight:700;padding-bottom:10px;border-bottom:1px solid rgba(255,255,255,.35);margin-bottom:14px}
.foot-col li{list-style:none;line-height:26px;display:flex;align-items:center;gap:8px}
.bullet{width:6px;height:6px;background:#fff;border-radius:50%}
.foot-col p{line-height:1.5}
.contact-item{display:flex;align-items:center;gap:10px;margin-top:12px}
.contact-item.phone{color:var(--yellow)}
.news-input{width:200px;height:26px;background:#fff;margin-top:12px;font-size:11px;color:#999;padding:6px 8px}
.news-btn{display:inline-block;margin-top:10px;background:var(--yellow);color:var(--ink);font-size:12px;font-weight:600;padding:5px 10px}
.social-dot{width:20px;height:20px;background:#fff;border-radius:3px}
.copyright{position:absolute;top:3965px;left:0;width:1200px;height:80px;background:var(--orange);color:#fff;text-align:center;font-size:13px;line-height:1.6;padding-top:20px}
</style>
</head>
<body>

<header class="site-header">
  <a class="brand" href="#">
    <span class="brand-dot" aria-hidden="true"></span>
    <span class="brand-name">Bright And Steady</span>
  </a>
  <nav class="main-nav">
    <a class="active" href="#">Home</a>
    <a href="#">About Us</a>
    <a href="#">Services &amp; Pricing</a>
    <a href="#">Our Team</a>
    <a href="#">Clients/Portfolio</a>
    <a href="#">Contact Us</a>
  </nav>
</header>

<section class="hero">
  <div class="hero-photo" role="img" aria-label="Photo of a smiling designer sketching at a desk in a bright office"></div>
  <div class="hero-shade"></div>
  <div class="hero-copy">
    <h1>The Bright And Steady Team That Always Puts Trust &amp; Loyalty Before Profits</h1>
    <p>Lorem ipsum dolor sit amet, consectetur adipiscing elit. In dignissim est dolor, vitae tempus magna mollis non. Mauris fermentum euismod maximus.</p>
    <div class="hero-actions">
      <a class="btn btn-orange" href="#">Contact Us Now</a>
      <a class="btn btn-red" href="#">Learn More</a>
    </div>
  </div>
</section>

<section class="services">
  <h2 class="section-title" style="top:52px">Our Services</h2>
  <svg class="divider" style="top:105px" viewBox="0 0 100 24" aria-hidden="true">
    <line x1="0" y1="12" x2="36" y2="12" stroke="#2b3a67" stroke-width="2"/>
    <line x1="64" y1="12" x2="100" y2="12" stroke="#2b3a67" stroke-width="2"/>
    <polygon points="50,2 53,9 61,9 55,14 57,22 50,17 43,22 45,14 39,9 47,9" fill="#f9a61a"/>
  </svg>
  <div class="service-grid">
    <div class="service">
      <svg width="90" height="90" viewBox="0 0 90 90" aria-hidden="true"><circle cx="45" cy="45" r="42" fill="#fff" stroke="#e0231b" stroke-width="2.5"/><circle cx="45" cy="45" r="32" fill="none" stroke="#1f1f24" stroke-width="2.5"/><rect x="30" y="34" width="30" height="20" fill="none" stroke="#1f1f24" stroke-width="2.5"/><line x1="45" y1="54" x2="45" y2="60" stroke="#1f1f24" stroke-width="2.5"/><line x1="37" y1="60" x2="53" y2="60" stroke="#1f1f24" stroke-width="2.5"/><line x1="35" y1="49" x2="48" y2="39" stroke="#e0231b" stroke-width="2.5"/></svg>
      <h3>Website Design &amp; Management</h3>
      <p>Sed eget magna non tortor imperdiet vestibulum. Quisque imperdietorci. Sed sollicitudin laoreet diam.</p>
    </div>
    <div class="service">
      <svg width="90" height="90" viewBox="0 0 90 90" aria-hidden="true"><circle cx="45" cy="45" r="42" fill="#fff" stroke="#e0231b" stroke-width="2.5"/><circle cx="45" cy="45" r="32" fill="none" stroke="#1f1f24" stroke-width="2.5"/><path d="M45 45c-6-8-16-8-16 0s10 8 16 0 16-8 16 0-10 8-16 0z" fill="none" stroke="#1f1f24" stroke-width="3"/></svg>
      <h3>Logo Design &amp; Branding Materials</h3>
      <p>Sed eget magna non tortor imperdiet vestibulum. Quisque imperdietorci. Sed sollicitudin laoreet diam.</p>
    </div>
    <div class="service">
      <svg width="90" height="90" viewBox="0 0 90 90" aria-hidden="true"><circle cx="45" cy="45" r="42" fill="#fff" stroke="#e0231b" stroke-width="2.5"/><circle cx="45" cy="45" r="32" fill="#1f1f24"/><rect x="30" y="36" width="30" height="20" fill="#fff"/><rect x="28" y="32" width="34" height="6" fill="#e0231b"/><rect x="35" y="42" width="8" height="14" fill="#1f1f24"/><rect x="47" y="42" width="9" height="7" fill="#1f1f24"/></svg>
      <h3>Online Store Design &amp; Management</h3>
      <p>Sed eget magna non tortor imperdiet vestibulum. Quisque imperdietorci. Sed sollicitudin laoreet diam.</p>
    </div>
    <div class="service">
      <svg width="90" height="90" viewBox="0 0 90 90" aria-hidden="true"><circle cx="45" cy="45" r="42" fill="#fff" stroke="#e0231b" stroke-width="2.5"/><circle cx="45" cy="45" r="32" fill="#1f1f24"/><circle cx="45" cy="45" r="23" fill="#fff"/><circle cx="45" cy="45" r="16" fill="#1f1f24"/><circle cx="45" cy="45" r="9" fill="#fff"/><circle cx="45" cy="45" r="4" fill="#e0231b"/></svg>
      <h3>Local SEO Management</h3>
      <p>Sed eget magna non tortor imperdiet vestibulum. Quisque imperdietorci. Sed sollicitudin laoreet diam.</p>
    </div>
    <div class="service">
      <svg width="90" height="90" viewBox="0 0 90 90" aria-hidden="true"><circle cx="45" cy="45" r="42" fill="#fff" stroke="#e0231b" stroke-width="2.5"/><circle cx="45" cy="45" r="32" fill="none" stroke="#1f1f24" stroke-width="2.5"/><circle cx="42" cy="42" r="11" fill="none" stroke="#1f1f24" stroke-width="3"/><line x1="50" y1="50" x2="60" y2="60" stroke="#e0231b" stroke-width="4"/></svg>
      <h3>Search Engine Optimization</h3>
      <p>Sed eget magna non tortor imperdiet vestibulum. Quisque imperdietorci. Sed sollicitudin laoreet diam.</p>
    </div>
    <div class="service">
      <svg width="90" height="90" viewBox="0 0 90 90" aria-hidden="true"><circle cx="45" cy="45" r="42" fill="#fff" stroke="#e0231b" stroke-width="2.5"/><circle cx="45" cy="45" r="32" fill="none" stroke="#1f1f24" stroke-width="2.5"/><circle cx="45" cy="45" r="6" fill="#e0231b"/><circle cx="33" cy="36" r="4" fill="#1f1f24"/><circle cx="57" cy="36" r="4" fill="#1f1f24"/><circle cx="45" cy="60" r="4" fill="#1f1f24"/><line x1="45" y1="45" x2="33" y2="36" stroke="#1f1f24" stroke-width="2"/><line x1="45" y1="45" x2="57" y2="36" stroke="#1f1f24" stroke-width="2"/><line x1="45" y1="45" x2="45" y2="60" stroke="#1f1f24" stroke-width="2"/></svg>
      <h3>Social Media Marketing</h3>
      <p>Sed eget magna non tortor imperdiet vestibulum. Quisque imperdietorci. Sed sollicitudin laoreet diam.</p>
    </div>
    <div class="service">
      <svg width="90" height="90" viewBox="0 0 90 90" aria-hidden="true"><circle cx="45" cy="45" r="42" fill="#fff" stroke="#e0231b" stroke-width="2.5"/><circle cx="45" cy="45" r="32" fill="none" stroke="#1f1f24" stroke-width="2.5"/><rect x="32" y="32" width="26" height="14" fill="none" stroke="#1f1f24" stroke-width="2.5"/><rect x="28" y="46" width="34" height="10" fill="#1f1f24"/><rect x="35" y="52" width="20" height="8" fill="#fff" stroke="#1f1f24" stroke-width="2"/><circle cx="56" cy="50" r="2" fill="#e0231b"/></svg>
      <h3>Marketing Material &amp; Print Design</h3>
      <p>Sed eget magna non tortor imperdiet vestibulum. Quisque imperdietorci. Sed sollicitudin laoreet diam.</p>
    </div>
    <div class="service">
      <svg width="90" height="90" viewBox="0 0 90 90" aria-hidden="true"><circle cx="45" cy="45" r="42" fill="#fff" stroke="#e0231b" stroke-width="2.5"/><circle cx="45" cy="45" r="32" fill="none" stroke="#1f1f24" stroke-width="2.5"/><circle cx="45" cy="45" r="6" fill="#e0231b"/><g stroke="#1f1f24" stroke-width="2.5"><line x1="45" y1="28" x2="45" y2="36"/><line x1="45" y1="54" x2="45" y2="62"/><line x1="28" y1="45" x2="36" y2="45"/><line x1="54" y1="45" x2="62" y2="45"/><line x1="33" y1="33" x2="39" y2="39"/><line x1="51" y1="51" x2="57" y2="57"/><line x1="57" y1="33" x2="51" y2="39"/><line x1="39" y1="51" x2="33" y2="57"/></g></svg>
      <h3>Outsourcing Management</h3>
      <p>Sed eget magna non tortor imperdiet vestibulum. Quisque imperdietorci. Sed sollicitudin laoreet diam.</p>
    </div>
  </div>
  <a class="btn btn-red" href="#">View More</a>
</section>

<section class="about">
  <svg class="band" width="1200" height="702" viewBox="0 0 1200 702" aria-hidden="true">
    <defs>
      <linearGradient id="aboutTone" x1="0" y1="0" x2="1" y2="1">
        <stop offset="0" stop-color="#e8352a"/>
        <stop offset="0.5" stop-color="#d9261d"/>
        <stop offset="1" stop-color="#e33a24"/>
      </linearGradient>
    </defs>
    <polygon points="0,0 1200,90 1200,620 0,702" fill="url(#aboutTone)"/>
    <polygon points="0,0 700,55 0,200" fill="#fbb911" opacity=".92"/>
    <polygon points="1200,470 1200,625 420,690" fill="#f9a61a" opacity=".92"/>
  </svg>
  <div role="img" aria-label="Red-toned photo of a team meeting around a table" style="position:absolute;inset:0"></div>
  <h2>About Us</h2>
  <div class="about-text">
    <p>We believe that honesty and integrity come before personal profits. We are a family owned and operated company. Our parents raised us to take care of each other and that's exactly what we've done. We treat each of our clients with the same loyalty and respect that we give each other.</p>
    <p>We are not looking to have hundreds and hundreds of clients. We are looking to expand our family with a handful of like-minded individuals. Companies who take pride in their work and their customers. We want to build mutually beneficial, lucrative, and long term partnerships.</p>
  </div>
  <a class="btn btn-orange" href="#">Who We Are</a>
</section>

<section class="features">
  <h2 class="section-title" style="top:0">Our Features</h2>
  <svg class="divider" style="top:53px" viewBox="0 0 100 24" aria-hidden="true">
    <line x1="0" y1="12" x2="36" y2="12" stroke="#2b3a67" stroke-width="2"/>
    <line x1="64" y1="12" x2="100" y2="12" stroke="#2b3a67" stroke-width="2"/>
    <polygon points="50,2 53,9 61,9 55,14 57,22 50,17 43,22 45,14 39,9 47,9" fill="#f9a61a"/>
  </svg>
  <div class="feature-row">
    <div class="feature">
      <svg width="64" height="58" viewBox="0 0 64 58" aria-hidden="true"><circle cx="24" cy="28" r="20" fill="#f9a61a"/><circle cx="46" cy="36" r="14" fill="#e0231b"/><text x="24" y="35" text-anchor="middle" font-family="Raleway,sans-serif" font-size="20" font-weight="800" fill="#fff">$</text><text x="46" y="41" text-anchor="middle" font-family="Raleway,sans-serif" font-size="14" font-weight="800" fill="#fff">$</text></svg>
      <h3>100% Risk Free Investment</h3>
      <p>If we are unable to deliver anything that we say we can we will refund you 100% of your investment.</p>
    </div>
    <div class="feature">
      <svg width="64" height="58" viewBox="0 0 64 58" aria-hidden="true"><circle cx="32" cy="29" r="22" fill="#f9a61a"/><circle cx="32" cy="29" r="16" fill="#fff"/><text x="32" y="35" text-anchor="middle" font-family="Raleway,sans-serif" font-size="16" font-weight="800" fill="#e0231b">24</text></svg>
      <h3>24/7 U.S. Based Customer Support</h3>
      <div class="contact-line"><svg width="12" height="14" viewBox="0 0 12 14" aria-hidden="true"><path d="M2 1h3l1 3-2 1c1 2 2 3 4 4l1-2 3 1v3c-6 0-10-4-10-10z" fill="#f9a61a"/></svg>555-014-2290</div>
      <div class="contact-line"><svg width="14" height="10" viewBox="0 0 14 10" aria-hidden="true"><rect width="14" height="10" fill="#f9a61a"/><path d="M0 0l7 5 7-5" fill="none" stroke="#fff" stroke-width="1.5"/></svg>hello@brightandsteady.example</div>
    </div>
    <div class="feature">
      <svg width="64" height="58" viewBox="0 0 64 58" aria-hidden="true"><rect x="10" y="16" width="40" height="28" rx="3" fill="#f9a61a"/><rect x="16" y="10" width="40" height="28" rx="3" fill="#e0231b"/><circle cx="36" cy="24" r="7" fill="#fff"/></svg>
      <h3>Customer Loyalty Program</h3>
      <p>After 12 months of on time payments Customers will receive cash back reward bonuses.</p>
    </div>
    <div class="feature">
      <svg width="64" height="58" viewBox="0 0 64 58" aria-hidden="true"><polygon points="32,4 40,16 35,16 35,30 29,30 29,16 24,16" fill="#e0231b"/><polygon points="8,48 14,34 17,39 29,32 32,37 20,44 23,48" fill="#f9a61a"/><polygon points="56,48 50,34 47,39 35,32 32,37 44,44 41,48" fill="#f9a61a"/></svg>
      <h3>Multiple Payment Options Available</h3>
      <p>Website Leasing, 30 Days Same As Cash, Website Financing.</p>
    </div>
  </div>
  <div class="feature feature-solo">
    <svg width="64" height="58" viewBox="0 0 64 58" aria-hidden="true"><circle cx="32" cy="18" r="11" fill="#f9a61a"/><path d="M12 56c0-14 9-22 20-22s20 8 20 22z" fill="#e0231b"/></svg>
    <h3>Unmatched Personal Service</h3>
    <p>Do you need us to come to your office to help train staff on the management of your new website, content management system, or computer software? That's not a problem. We will come to you and provide hands on training.</p>
  </div>
</section>

<section class="team">
  <h2 class="section-title" style="top:68px">Our Team</h2>
  <svg class="divider" style="top:121px" viewBox="0 0 100 24" aria-hidden="true">
    <line x1="0" y1="12" x2="36" y2="12" stroke="#2b3a67" stroke-width="2"/>
    <line x1="64" y1="12" x2="100" y2="12" stroke="#2b3a67" stroke-width="2"/>
    <polygon points="50,2 53,9 61,9 55,14 57,22 50,17 43,22 45,14 39,9 47,9" fill="#f9a61a"/>
  </svg>
  <div class="team-grid">
    <div class="member"><div class="member-photo" role="img" aria-label="Portrait photo of Arlo Bennett"></div><h4>Arlo Bennett</h4><span>Chief Executive Officer</span></div>
    <div class="member"><div class="member-photo" role="img" aria-label="Portrait photo of Mara Quill"></div><h4>Mara Quill</h4><span>Chief Operations Officer</span></div>
    <div class="member"><div class="member-photo" role="img" aria-label="Portrait photo of Dev Sorel"></div><h4>Dev Sorel</h4><span>Chief Technical Officer</span></div>
    <div class="member"><div class="member-photo" role="img" aria-label="Portrait photo of Owen Trask"></div><h4>Owen Trask</h4><span>Finance Officer</span></div>
    <div class="member"><div class="member-photo" role="img" aria-label="Portrait photo of Felix Harrow"></div><h4>Felix Harrow</h4><span>Chief Executive Officer</span></div>
  </div>
</section>

<section class="clients">
  <h2 class="section-title" style="top:62px">Our Clients</h2>
  <svg class="divider" style="top:115px" viewBox="0 0 100 24" aria-hidden="true">
    <line x1="0" y1="12" x2="36" y2="12" stroke="#2b3a67" stroke-width="2"/>
    <line x1="64" y1="12" x2="100" y2="12" stroke="#2b3a67" stroke-width="2"/>
    <polygon points="50,2 53,9 61,9 55,14 57,22 50,17 43,22 45,14 39,9 47,9" fill="#f9a61a"/>
  </svg>
  <div class="client-row">
    <div class="client">Northwire</div>
    <div class="client">Ridgeview College</div>
    <div class="client"><i></i>Valley Power Co.</div>
    <div class="client"><i></i>Quarklight</div>
    <div class="client">Bluestem</div>
    <div class="client">The Summit Forum</div>
  </div>
</section>

<footer class="site-footer">
  <div class="foot-col" style="left:81px;width:170px">
    <h4>Quick Links</h4>
    <ul>
      <li><span class="bullet"></span>Home</li>
      <li><span class="bullet"></span>About Us</li>
      <li><span class="bullet"></span>Services &amp; Pricing</li>
      <li><span class="bullet"></span>Our Team</li>
      <li><span class="bullet"></span>Clients/Portfolio</li>
      <li><span class="bullet"></span>Contact Us</li>
    </ul>
  </div>
  <div class="foot-col" style="left:318px;width:280px">
    <h4>Contact Information</h4>
    <p>Suspendisse convallis ex eu velit dapibus erat consequat.</p>
    <div class="contact-item"><svg width="12" height="16" viewBox="0 0 12 16" aria-hidden="true"><path d="M6 0a6 6 0 0 1 6 6c0 4-6 10-6 10S0 10 0 6a6 6 0 0 1 6-6z" fill="#fff"/><circle cx="6" cy="6" r="2" fill="#e0231b"/></svg>118 Maple Row, Lakeside</div>
    <div class="contact-item phone"><svg width="12" height="14" viewBox="0 0 12 14" aria-hidden="true"><path d="M2 1h3l1 3-2 1c1 2 2 3 4 4l1-2 3 1v3c-6 0-10-4-10-10z" fill="#fff"/></svg>555 018 3341</div>
    <div class="contact-item"><svg width="14" height="10" viewBox="0 0 14 10" aria-hidden="true"><rect width="14" height="10" fill="#fff"/><path d="M0 0l7 5 7-5" fill="none" stroke="#e0231b" stroke-width="1.5"/></svg>info@BrightAndSteady.example</div>
  </div>
  <div class="foot-col" style="left:655px;width:250px">
    <h4>Newsletter Signup</h4>
    <p>Please enter your email address below to receive our FREE newsletter</p>
    <div class="news-input">Your Email ID</div>
    <span class="news-btn">Subscribe</span>
  </div>
  <div class="foot-col" style="left:950px;width:170px">
    <h4>Follow Us</h4>
    <ul>
      <li><span class="social-dot"></span>Social Feed</li>
      <li><span class="social-dot"></span>Pro Network</li>
      <li><span class="social-dot"></span>Microblog</li>
      <li><span class="social-dot"></span>Email</li>
    </ul>
  </div>
</footer>
<div class="copyright">© 2017 All Rights Reserved. Business policy<br>Made with care by Bright And Steady</div>

</body>
</html>
```